Whitlow Bidhouse on responsive WP

We need a wordpress design for an established auction and real estate company based in Texas. The winning design will incorporate a professional color scheme with company logo in a clean layout. The design needs to consider that this will be developed on a responsive theme. Colors are those that will highlight the logo.

Industry/Entity Type

Real Estate

Font styles to use
Sans Serif

Colors

Designer to choose colors to be used in the design.

Requirements
Must have
• navigation: 1) home 2) Auctions 3) Online Auctions 4) For Sale 5) About Us 6) Our Services 7) Contact Us

design will have slideshow element, either use the attached image or a stock image if it better fits your design

Widgets in the Sidebar: 1) email signup form 2) social media icons - facebook, pinterest, linkedIn, Youtube 3) Featured Auctions widget 4) News& Events blog

footer will have smaller company logo, contact info (below) and attached association logos.

Colors will be that of the logo and white, black/gray and perhaps another highlight color.

Phone: (555) 384-2706
Email: whitlowbidhouse@mailbarn.example
Address: 2715 Marrow Lane, Dellford, TX 70000
Nice to have
• Use of drop menus - for example 1) Upcoming Auctions and 2) Past Auctions under the menu item "Auctions"

```html
<!DOCTYPE html>
<html lang="en">
<head>
<meta charset="utf-8">
<title>Whitlow Bidhouse</title>
<link href="https://fonts.googleapis.com/css2?family=Open+Sans:wght@400;600;700&display=swap" rel="stylesheet">
<style>
:root{
  --red:#c0141b;
  --blue:#0b5fbf;
  --nav:#3a3a3a;
  --nav-line:#555;
  --ink:#444;
  --muted:#888;
  --hero:#ebe2d2;
  --side:#f0f0f0;
  --foot:#f4f4f4;
  --base:#2b2b2b;
  --line:#ddd;
}
*{box-sizing:border-box;margin:0;padding:0}
html,body{width:738px;height:1200px;overflow:hidden;background:#fff}
body{position:relative;font-family:"Open Sans",Arial,sans-serif;color:var(--ink)}
.abs{position:absolute}

/* header */
.brand{left:61px;top:42px;display:flex;align-items:center;gap:7px}
.brand-mark{width:16px;height:16px;background:var(--red);flex:none}
.brand-name{font-size:17px;font-weight:700;color:var(--red);line-height:1;white-space:nowrap}
.contact-top{right:61px;top:30px;text-align:right;line-height:1.35}
.contact-top .phone{font-size:14px;color:var(--red);font-weight:600}
.contact-top .mail{font-size:9.5px;color:var(--blue)}
.contact-top .addr{font-size:8.5px;color:#777;margin-top:5px}

/* hero */
.hero{left:0;top:122px;width:738px;height:267px;background:var(--hero)}
.hero-photo{left:346px;top:150px;width:330px;height:222px;border-radius:6px;background:linear-gradient(135deg,#595959 0%,#3e3e3e 45%,#3a3a3a 62%,#8a4520 80%,#d8ccb8 100%)}
.hero-title{left:73px;top:185px;font-size:20px;color:var(--red);font-weight:400}
.hero-text{left:73px;top:215px;width:245px;font-size:9px;line-height:1.55;color:#555}
.btn-bid{left:74px;top:269px;width:65px;height:25px;background:#3a3a3a;color:#fff;font-size:11px;display:flex;align-items:center;justify-content:center;border-radius:2px}
.slide-nav{left:73px;top:313px}

/* nav */
.nav{left:61px;top:108px;width:616px;height:28px;background:var(--nav);display:flex}
.nav a{color:#fff;font-size:8.5px;text-decoration:none;display:flex;align-items:center;padding:0 10px;border-right:1px solid var(--nav-line)}
.nav a.active{background:var(--blue)}
.nav .search{margin-left:auto;width:130px;display:flex;align-items:center;justify-content:space-between;padding-left:12px;font-size:8.5px;color:#aaa}
.nav .search-btn{width:26px;height:28px;background:#2a2a2a;display:flex;align-items:center;justify-content:center}
.dropdown{left:109px;top:136px;width:103px;height:49px;background:var(--blue);padding:9px 0 0 10px;font-size:8.5px;color:#fff;line-height:19px}

/* auctions grid */
.section-title{font-size:13px;color:var(--blue);font-weight:400}
.grid{left:62px;top:436px;display:grid;grid-template-columns:repeat(3,141px);grid-auto-rows:165px;column-gap:10px;row-gap:15px}
.card{border:1px solid var(--line);padding:4px;text-align:center}
.card-photo{height:90px}
.card h3{font-size:10px;font-weight:400;color:#444;margin-top:10px}
.card p{font-size:7.5px;color:var(--muted);line-height:1.6;margin-top:4px}

/* sidebar */
.sidebar{left:523px;top:390px;width:154px;height:587px;background:var(--side)}
.side-rule{left:523px;width:154px;height:1px;background:#d8d8d8}
.field{left:530px;top:429px;width:139px;height:22px;background:#fff;border:1px solid var(--line);font-size:7.5px;color:#aaa;padding:6px 8px}
.btn-sub{left:604px;top:458px;width:64px;height:16px;background:#555;color:#fff;font-size:7px;display:flex;align-items:center;justify-content:center;border-radius:2px}
.feat{left:530px;width:139px;height:53px;background:#fff;border:1px solid #e4e4e4;display:flex;padding:3px;gap:8px}
.feat-photo{width:45px;height:45px;flex:none}
.feat p{font-size:8.5px;color:#777;line-height:1.4;margin-top:4px}
.tabs{left:530px;top:722px;width:139px;height:24px;display:flex;font-size:9px}
.tabs span{display:flex;align-items:center;justify-content:center;color:#fff;background:#888;flex:1;border-left:1px solid #aaa}
.tabs span.on{background:#fff;color:#666;border:none}
.newsbox{left:530px;top:746px;width:139px;height:186px;background:#fff;padding:4px}
.news-photo{height:69px}
.newsbox h4{font-size:7.5px;font-weight:600;color:#555;margin:12px 4px 0;line-height:1.5;text-transform:uppercase}
.newsbox p{font-size:7px;color:#999;line-height:1.6;margin:5px 4px 0}
.newsbox .more{font-size:7.5px;color:#555;margin:8px 4px 0;text-transform:uppercase}
.social{left:535px;top:944px;display:flex;gap:7px}
.social span{width:20px;height:20px;border-radius:50%}

/* footer */
.footer{left:0;top:977px;width:738px;height:155px;background:var(--foot)}
.fcol{top:996px;width:145px}
.fcol h5{font-size:10.5px;font-weight:400;color:#444;margin-bottom:11px}
.fcol p{font-size:7.5px;line-height:1.7;color:#888}
.fcol .strong{font-weight:600;color:#555;font-size:8px}
.fcol .link{font-size:7.5px;color:var(--blue);margin-top:5px}
.fcol .email{font-size:6.8px;color:var(--blue);white-space:nowrap}
.fdiv{top:995px;width:1px;height:127px;background:#ddd}
.badges{left:540px;top:1023px;display:flex;gap:8px}
.badges span{width:28px;height:28px;border-radius:50%;background:#9aa3ad}
.badges span.sq{border-radius:3px;background:#4a4a4a}
.flogo{left:537px;top:1078px;display:flex;align-items:center;gap:5px}
.flogo i{width:10px;height:10px;background:#aaa;flex:none}
.flogo b{font-size:10px;font-weight:700;color:#999;white-space:nowrap}

.base{left:0;top:1132px;width:738px;height:68px;background:var(--base);color:#bbb;text-align:center}
.base-nav{font-size:7.5px;margin-top:22px;word-spacing:2px}
.base-copy{font-size:7.5px;margin-top:13px}
</style>
</head>
<body>

<header>
  <div class="abs brand"><span class="brand-mark"></span><span class="brand-name">WHITLOW BIDHOUSE</span></div>
  <div class="abs contact-top">
    <div class="phone">Phone: (555) 384-2706</div>
    <div class="mail">Email: whitlowbidhouse@mailbarn.example</div>
    <div class="addr">2715 Marrow Lane, Dellford, TX 70000</div>
  </div>
</header>

<section>
  <div class="abs hero"></div>
  <div class="abs hero-photo" role="img" aria-label="Antique two-barrel pocket pistol with wooden grip"></div>
  <h1 class="abs hero-title">Aliquam imperdiet</h1>
  <p class="abs hero-text">Cum sociis natoque penatibus et magnis dis parturient montes, nascetur ridiculus mus. Etiam congue risus quis orci bibendum adipiscing.</p>
  <div class="abs btn-bid">Bid Now</div>
  <svg class="abs slide-nav" width="28" height="28" viewBox="0 0 28 28">
    <circle cx="14" cy="14" r="13" fill="#444" stroke="#888" stroke-width="1.5"/>
    <path d="M12 10l-4 4 4 4M16 10l4 4-4 4" stroke="#fff" stroke-width="1.6" fill="none"/>
  </svg>
</section>

<nav class="abs nav">
  <a href="#">HOME</a><a href="#" class="active">AUCTIONS</a><a href="#">ONLINE AUCTIONS</a><a href="#">FOR SALE</a><a href="#">ABOUT US</a><a href="#">OUR SERVICES</a><a href="#">CONTACT US</a>
  <div class="search">Search
    <span class="search-btn"><svg width="11" height="11" viewBox="0 0 11 11"><circle cx="4.5" cy="4.5" r="3.3" stroke="#fff" stroke-width="1.5" fill="none"/><path d="M7 7l3 3" stroke="#fff" stroke-width="1.6"/></svg></span>
  </div>
</nav>
<div class="abs dropdown">• Upcoming Auctions<br>• Past Auctions</div>

<main>
  <h2 class="abs section-title" style="left:62px;top:408px">LATEST AUCTIONS</h2>
  <svg class="abs" style="left:496px;top:411px" width="10" height="10" viewBox="0 0 10 10"><circle cx="5" cy="5" r="4.3" fill="none" stroke="#bbb"/><path d="M4 3l3 2-3 2z" fill="#bbb"/></svg>
  <div class="abs grid">
    <div class="card"><div class="card-photo" role="img" aria-label="Banquet room with display tables" style="background:linear-gradient(180deg,#8a6a3a,#b89a68)"></div><h3>Curabitur pulvinar urna</h3><p>Sat Aug 23 - 01:00PM<br>Dellford, TX</p></div>
    <div class="card"><div class="card-photo" role="img" aria-label="Vintage twin-lens camera" style="background:linear-gradient(180deg,#e6e6e6,#cfcfcf)"></div><h3>Curabitur pulvinar urna</h3><p>Sat Aug 23 - 01:00PM<br>Dellford, TX</p></div>
    <div class="card"><div class="card-photo" role="img" aria-label="White minivan" style="background:linear-gradient(180deg,#8a9380,#d8d8d6)"></div><h3>Curabitur pulvinar urna</h3><p>Sat Aug 23 - 01:00PM<br>Dellford, TX</p></div>
    <div class="card"><div class="card-photo" role="img" aria-label="Fishing gear laid out" style="background:linear-gradient(180deg,#ececec,#dcd6cc)"></div><h3>Curabitur pulvinar urna</h3><p>Sat Aug 23 - 01:00PM<br>Dellford, TX</p></div>
    <div class="card"><div class="card-photo" role="img" aria-label="Golf cart in a showroom" style="background:linear-gradient(180deg,#7a6a50,#a89880)"></div><h3>Curabitur pulvinar urna</h3><p>Sat Aug 23 - 01:00PM<br>Dellford, TX</p></div>
    <div class="card"><div class="card-photo" role="img" aria-label="Vintage computer board and keyboard" style="background:linear-gradient(180deg,#cfcac2,#a88a62)"></div><h3>Curabitur pulvinar urna</h3><p>Sat Aug 23 - 01:00PM<br>Dellford, TX</p></div>
    <div class="card"><div class="card-photo" role="img" aria-label="Row of ancient coins" style="background:#eeeeee"></div><h3>Curabitur pulvinar urna</h3><p>Sat Aug 23 - 01:00PM<br>Dellford, TX</p></div>
    <div class="card"><div class="card-photo" role="img" aria-label="Makeup palette in a case" style="background:#ececec"></div><h3>Curabitur pulvinar urna</h3><p>Sat Aug 23 - 01:00PM<br>Dellford, TX</p></div>
    <div class="card"><div class="card-photo" role="img" aria-label="Stone bead bracelet" style="background:linear-gradient(180deg,#d4d2cc,#a8a294)"></div><h3>Curabitur pulvinar urna</h3><p>Sat Aug 23 - 01:00PM<br>Dellford, TX</p></div>
  </div>
</main>

<aside>
  <div class="abs sidebar"></div>
  <h2 class="abs section-title" style="left:530px;top:408px">NEWSLETTER SIGNUP</h2>
  <div class="abs field">E-mail ID</div>
  <div class="abs btn-sub">Subscribe now</div>
  <div class="abs side-rule" style="top:489px"></div>

  <h2 class="abs section-title" style="left:530px;top:506px">FEATURED ACTIONS</h2>
  <div class="abs feat" style="top:526px"><div class="feat-photo" role="img" aria-label="Collectible action figure" style="background:linear-gradient(180deg,#6a655e,#c8c0b2)"></div><p>Cum sociis<br>natoque penatibus</p></div>
  <div class="abs feat" style="top:581px"><div class="feat-photo" role="img" aria-label="Classic red car" style="background:linear-gradient(180deg,#b8b0a0,#8a4a38)"></div><p>Cum sociis<br>natoque penatibus</p></div>
  <div class="abs feat" style="top:635px"><div class="feat-photo" role="img" aria-label="Two-storey house" style="background:linear-gradient(180deg,#7a9a6a,#b89888)"></div><p>Cum sociis<br>natoque penatibus</p></div>
  <div class="abs side-rule" style="top:707px"></div>

  <div class="abs tabs"><span class="on">NEWS</span><span>EVENTS</span><span>BLOG</span></div>
  <div class="abs newsbox">
    <div class="news-photo" role="img" aria-label="Lit mansion beside a pool at dusk" style="background:linear-gradient(180deg,#3a5a8a,#6a7a90 55%,#2a3a5a)"></div>
    <h4>Aliquam imperdiet nulla id risus tincidunt sagittis.</h4>
    <p>Nulla facilisi. Vestibulum mollis dignissim dui fringilla adipiscing. Nam turpis augue, sagittis eu nisl non, fermentum imperdiet odio.</p>
    <div class="more">Read more</div>
  </div>
  <div class="abs social">
    <span style="background:#3b5998"></span><span style="background:#2a86b8"></span><span style="background:#cb2027"></span><span style="background:#e02a20"></span><span style="background:#6aa83a"></span>
  </div>
</aside>

<footer>
  <div class="abs footer"></div>
  <div class="abs fcol" style="left:62px">
    <h5>About Us</h5>
    <p>Curabitur nec lectus euismod, luctus lorem sit amet, iaculis magna. Nulla facilisi. Vestibulum mollis dignissim dui fringilla adipiscing. Nam turpis augue, sagittis eu nisl non, fermentum imperdiet odio.</p>
    <p class="link">Know more</p>
  </div>
  <div class="abs fdiv" style="left:213px"></div>
  <div class="abs fcol" style="left:229px;width:140px">
    <h5>Latest Blog</h5>
    <p class="strong">Morbi sit amet consequat diam</p>
    <p>Cras faucibus sapien at arcu dignissim interdum. Sed tempus leo nulla, eget auctor tortor pharetra a. Morbi et gravida tortor, vitae cursus odio amet felis eleifend molestie</p>
    <p class="link">Know more</p>
  </div>
  <div class="abs fdiv" style="left:382px"></div>
  <div class="abs fcol" style="left:396px;width:128px">
    <h5>Contact us</h5>
    <p>Address: 2715 Marrow Lane,<br>Dellford, TX 70000</p>
    <p style="margin-top:6px">Phone: (555) 384-2706</p>
    <p style="margin-top:6px">E-mail :</p>
    <p class="email">whitlowbidhouse@mailbarn.example</p>
  </div>
  <div class="abs fdiv" style="left:528px"></div>
  <div class="abs badges"><span class="sq"></span><span></span><span style="background:#8aa0c0"></span><span style="background:#2a6aa0"></span></div>
  <div class="abs flogo"><i></i><b>WHITLOW BIDHOUSE</b></div>

  <div class="abs base">
    <div class="base-nav">Home &nbsp;| &nbsp;Auctions &nbsp;| &nbsp;Online Auctions &nbsp;| &nbsp;For Sale &nbsp;| &nbsp;About Us &nbsp;| &nbsp;Our Services &nbsp;| &nbsp;Contact Us</div>
    <div class="base-copy">Copyright © 2014 Whitlow Bidhouse. &nbsp;All rights reserved.</div>
  </div>
</footer>

</body>
</html>
```